Pipelining Product Supply Company Needs New Stationery

We need new stationery (letter head, with compliments slips & business card) for our industry leading pipe lining supply company. basically we sell product to other plumbers to carry out pipe relining.

Im looking for something, fresh, professional, sleek and modern at the same time.

Ive attached a copy of the logo and also some guidelines to follow for colours and fonts etc.

Target Market(s)

Plumbers

Industry/Entity Type

Plumbing

Font styles to use
Sans Serif

Requirements
Must have
• The logo, space for ABN, Address, Phone Number, website and email.
Nice to have
• Stand out from the crowd. To look sleep and professional.
Should not have
• Any other colours apart from what is on the guidelines.

```html
<!DOCTYPE html>
<html lang="en">
<head>
<meta charset="utf-8">
<title>Keelbrook Pipelining Supplies – Business Card</title>
<link href="https://fonts.googleapis.com/css2?family=Roboto:wght@400;500&family=Roboto+Condensed:wght@700&display=swap" rel="stylesheet">
<style>
  :root {
    --backdrop: #2b2b2d;
    --card: #1f1f21;
    --green: #8dc63f;
    --white: #f2f2f2;
    --grey: #9a9a9c;
    --rule: #5a5a5c;
  }
  * { margin: 0; padding: 0; box-sizing: border-box; }
  html, body { width: 1200px; height: 900px; overflow: hidden; }
  body {
    background: var(--backdrop);
    font-family: "Roboto", Arial, sans-serif;
    display: flex;
    flex-direction: column;
    align-items: center;
    justify-content: center;
    gap: 44px;
  }
  .card {
    width: 760px;
    height: 380px;
    background: var(--card);
    border-radius: 4px;
    position: relative;
    box-shadow: 0 8px 24px rgba(0,0,0,0.35);
  }
  /* Front */
  .card-front {
    display: flex;
    flex-direction: column;
    align-items: center;
    justify-content: center;
  }
  .brand {
    display: flex;
    align-items: center;
    gap: 16px;
  }
  .brand-dot {
    width: 22px; height: 22px;
    border-radius: 50%;
    background: var(--green);
  }
  .brand-name {
    color: var(--green);
    font-family: "Roboto", Arial, sans-serif;
    font-weight: 500;
    font-size: 38px;
    letter-spacing: 2px;
    text-transform: uppercase;
    line-height: 1.15;
  }
  .brand-name span { display: block; }
  .front-web {
    margin-top: 46px;
    color: var(--white);
    font-size: 17px;
    letter-spacing: 2.5px;
  }
  /* Back */
  .card-back { padding-top: 104px; }
  .back-top {
    display: flex;
    justify-content: center;
    align-items: center;
    gap: 34px;
  }
  .person { text-align: right; }
  .person-name {
    font-family: "Roboto Condensed", Arial, sans-serif;
    font-weight: 700;
    font-size: 38px;
    color: var(--green);
    letter-spacing: 0.5px;
    line-height: 1;
  }
  .person-role {
    font-size: 17px;
    color: var(--grey);
    letter-spacing: 1px;
    margin-top: 4px;
  }
  .divider { width: 1px; height: 86px; background: var(--rule); }
  .contacts { list-style: none; }
  .contacts li {
    display: flex;
    align-items: center;
    gap: 12px;
    color: var(--white);
    font-size: 18px;
    line-height: 27px;
  }
  .contacts svg, .address svg { width: 16px; height: 16px; fill: var(--green); flex: none; }
  .back-bottom {
    margin-top: 56px;
    text-align: center;
    color: var(--white);
    font-size: 18px;
    line-height: 28px;
  }
  .address { display: inline-flex; align-items: center; gap: 6px; }
</style>
</head>
<body>
  <section class="card card-front">
    <div class="brand">
      <div class="brand-dot"></div>
      <div class="brand-name"><span>Keelbrook</span><span>Pipelining Supplies</span></div>
    </div>
    <p class="front-web">www.keelbrookpipelining.com</p>
  </section>

  <section class="card card-back">
    <div class="back-top">
      <div class="person">
        <p class="person-name">DANIEL HARPER</p>
        <p class="person-role">CEO/FOUNDER</p>
      </div>
      <div class="divider"></div>
      <ul class="contacts">
        <li>
          <svg viewBox="0 0 16 16" aria-hidden="true"><path d="M3.6 1.2l2.2 2.9-1.3 1.7c.9 2 2.6 3.7 4.6 4.6l1.7-1.3 2.9 2.2-1.3 2.6C7.4 13.7 2.3 8.6 1 3.6z"/></svg>
          555 014 2271
        </li>
        <li>
          <svg viewBox="0 0 16 16" aria-hidden="true"><path d="M1 3h14v10H1z M2 4.2v.4l6 4.2 6-4.2v-.4z" fill-rule="evenodd"/></svg>
          info@keelbrook.com
        </li>
        <li>
          <svg viewBox="0 0 16 16" aria-hidden="true"><circle cx="8" cy="8" r="7"/></svg>
          www.keelbrook.com
        </li>
      </ul>
    </div>
    <div class="back-bottom">
      <p class="address">
        <svg viewBox="0 0 16 16" aria-hidden="true"><path d="M8 0a5.5 5.5 0 0 0-5.5 5.5C2.5 10 8 16 8 16s5.5-6 5.5-10.5A5.5 5.5 0 0 0 8 0zm0 8a2.5 2.5 0 1 1 0-5 2.5 2.5 0 0 1 0 5z"/></svg>
        42 Harbour Street, Newcastle, NSW 2300
      </p>
      <p>ABN: 9081726354</p>
    </div>
  </section>
</body>
</html>
```